New business card for our new logo

I have a brand new, existing logo. Now I need it on a new business card. The new card should include the following:

English language training
Translations
Interpreting Services (remote and in-person)

Target Market(s)

We are targeting international companies with foreign investment in the United States as well as domestic companies, medical offices, law offices, and non-profits that have non-native English speakers as their clients.

Contact Information for Business Card

Marla Quennet, President
418 Garvin St.
Indianapolis, IN 46871
(317) 584-2316
info@brightpathwordworks.com
www.brightpathwordworks.com

Font styles to use
Sans Serif

Colors
0392cd
3176b5
abd036
9bcb3b
f04a50
f78f20

Requirements
Must have
• It must include our logo and business card details
Nice to have
• I would like to see a layout that is uncluttered and conveys trust and dependability, as well as the feelings of being friendly and approachable.

It would be nice to have icons for English language training, translating, and interpreting.
Should not have
• No pink, yellow, or purple

```html
<!DOCTYPE html>
<html lang="en">
<head>
<meta charset="utf-8">
<title>Brightpath Wordworks — Stationery</title>
<link rel="stylesheet" href="https://fonts.googleapis.com/css2?family=Roboto:wght@400;500;700&display=swap">
<style>
  :root{
    --navy:#1f3b6d;
    --ink:#4a4f57;
    --muted:#6b7079;
    --paper:#ffffff;
    --stage:#e6e7ea;
    --rule:#9aa3b2;
    --sign:#eef0f3;
  }
  *{margin:0;padding:0;box-sizing:border-box}
  html,body{width:1200px;height:894px;overflow:hidden;background:var(--stage);font-family:"Roboto",Arial,sans-serif;color:var(--ink)}
  .canvas{position:relative;width:1200px;height:894px}

  .card{position:absolute;left:60px;width:420px;height:240px;box-shadow:0 2px 8px rgba(0,0,0,.12)}
  .brand{display:flex;align-items:center;gap:10px}
  .brand-dot{border-radius:50%;flex:none}
  .brand-name{font-weight:500;line-height:1.02}

  /* front */
  .card-front{top:170px;background:var(--paper)}
  .card-front .brand{position:absolute;top:34px;right:36px}
  .card-front .brand-dot{width:44px;height:44px;background:var(--navy)}
  .card-front .brand-name{color:var(--navy);font-size:17px}
  .card-front .rule{position:absolute;left:36px;right:36px;top:100px;height:1px;background:var(--rule)}
  .card-front .address{position:absolute;right:36px;top:110px;text-align:right;font-size:10px;line-height:1.4;color:var(--muted)}
  .card-front .person{position:absolute;left:36px;bottom:26px}
  .person-name{font-size:15px;font-weight:700;color:var(--navy)}
  .person-title{font-size:11px;color:var(--muted);margin-bottom:6px}
  .contact-line{display:flex;align-items:center;gap:5px;font-size:10px;line-height:1.45;color:var(--muted)}
  .contact-line svg{width:9px;height:9px;fill:var(--navy);flex:none}

  /* back */
  .card-back{top:450px;background:var(--navy);color:#fff}
  .card-back .brand{position:absolute;left:60px;top:58px;gap:16px}
  .card-back .brand-dot{width:80px;height:80px;background:#fff}
  .card-back .brand-name{color:#fff;font-size:25px}
  .services{position:absolute;left:24px;right:24px;bottom:18px;display:flex;justify-content:space-between;font-size:10px}
  .service{display:flex;align-items:center;gap:5px}
  .service svg{width:12px;height:12px;stroke:#fff;fill:none;stroke-width:1.4}

  /* letterhead */
  .letterhead{position:absolute;left:570px;top:24px;width:596px;height:846px;background:var(--paper);box-shadow:0 3px 12px rgba(0,0,0,.14);padding:0 66px}
  .letterhead .brand{justify-content:center;margin-top:52px}
  .letterhead .brand-dot{width:46px;height:46px;background:var(--navy)}
  .letterhead .brand-name{color:var(--navy);font-size:17px}
  .letter-body{margin-top:70px;font-size:11.2px;line-height:1.45;color:var(--ink)}
  .letter-body p{margin-bottom:14px}
  .signature{width:130px;height:56px;background:var(--sign);border-radius:4px;margin-top:10px}
  .letter-footer{position:absolute;right:50px;bottom:40px;text-align:right;font-size:11px;line-height:1.6;color:var(--muted)}
  .letter-footer strong{color:var(--navy);font-weight:700}
  .letter-footer .contact-row{display:flex;justify-content:flex-end;gap:12px}
  .letter-footer .contact-line{font-size:11px}
</style>
</head>
<body>
<main class="canvas">
  <svg width="0" height="0" style="position:absolute">
    <defs>
      <symbol id="icon-phone" viewBox="0 0 24 24"><path d="M6.6 10.8a15 15 0 0 0 6.6 6.6l2.2-2.2c.3-.3.7-.4 1-.2 1.1.4 2.3.6 3.6.6.6 0 1 .4 1 1V20c0 .6-.4 1-1 1A17 17 0 0 1 3 4c0-.6.4-1 1-1h3.5c.6 0 1 .4 1 1 0 1.3.2 2.5.6 3.6.1.3 0 .7-.2 1z"/></symbol>
      <symbol id="icon-mail" viewBox="0 0 24 24"><path d="M2 5h20v14H2zM4 7v.5l8 5 8-5V7l-8 5z"/></symbol>
      <symbol id="icon-web" viewBox="0 0 24 24"><path d="M12 2a10 10 0 1 0 0 20 10 10 0 0 0 0-20zm0 2c1 1.3 1.8 3 2.1 5H9.9C10.2 7 11 5.3 12 4zM4.3 14a8 8 0 0 1 0-4h3.5a17 17 0 0 0 0 4zm.8 2h3a13 13 0 0 0 1.4 3.5A8 8 0 0 1 5.1 16zm3-8h-3a8 8 0 0 1 4.4-3.5A13 13 0 0 0 8.1 8zM12 20c-1-1.3-1.8-3-2.1-5h4.2c-.3 2-1.1 3.7-2.1 5zm2.3-7H9.7a15 15 0 0 1 0-2h4.6a15 15 0 0 1 0 2zm.2 6.5A13 13 0 0 0 15.9 16h3a8 8 0 0 1-4.4 3.5zM16.2 14a17 17 0 0 0 0-4h3.5a8 8 0 0 1 0 4z"/></symbol>
    </defs>
  </svg>

  <section class="card card-front" aria-label="Business card front">
    <div class="brand"><span class="brand-dot"></span><span class="brand-name">Brightpath<br>Wordworks</span></div>
    <div class="rule"></div>
    <div class="address">418 Garvin St.<br>Indianapolis, IN 46871</div>
    <div class="person">
      <div class="person-name">Marla Quennet</div>
      <div class="person-title">President</div>
      <div class="contact-line"><svg><use href="#icon-phone"/></svg>(317) 584-2316</div>
      <div class="contact-line"><svg><use href="#icon-mail"/></svg>info@brightpathwordworks.com</div>
      <div class="contact-line"><svg><use href="#icon-web"/></svg>www.brightpathwordworks.com</div>
    </div>
  </section>

  <section class="card card-back" aria-label="Business card back">
    <div class="brand"><span class="brand-dot"></span><span class="brand-name">Brightpath<br>Wordworks</span></div>
    <div class="services">
      <span class="service"><svg viewBox="0 0 12 12"><rect x="1" y="2" width="10" height="7"/><path d="M4 11h4"/></svg>English language training</span>
      <span class="service"><svg viewBox="0 0 12 12"><rect x="1" y="1" width="6" height="6"/><rect x="5" y="5" width="6" height="6"/></svg>Translations</span>
      <span class="service"><svg viewBox="0 0 12 12"><circle cx="3.5" cy="3.5" r="1.6"/><circle cx="8.5" cy="3.5" r="1.6"/><path d="M1 10c0-2 1-3 2.5-3S6 8 6 10M6 10c0-2 1-3 2.5-3S11 8 11 10"/></svg>Interpreting Services</span>
    </div>
  </section>

  <article class="letterhead" aria-label="Letterhead">
    <div class="brand"><span class="brand-dot"></span><span class="brand-name">Brightpath<br>Wordworks</span></div>
    <div class="letter-body">
      <p>Dear customer,</p>
      <p>Lorem ipsum dolor sit amet, consectetur adipisicing elit, sed do eiusmod tempor incididunt ut labore et dolore magna aliqua. Ut enim ad minim veniam, quis nostrud exercitation ullamco laboris nisi ut aliquip ex ea commodo consequat. Duis aute irure dolor in reprehenderit in voluptate velit esse cillum dolore eu fugiat nulla pariatur. Excepteur sint occaecat cupidatat non proident, sunt in culpa qui officia deserunt mollit anim id est laborum.</p>
      <p>Lorem ipsum dolor sit amet, consectetur adipisicing elit, sed do eiusmod tempor incididunt ut labore et dolore magna aliqua. Ut enim ad minim veniam, quis nostrud exercitation ullamco laboris nisi ut aliquip ex ea commodo consequat. Duis aute irure dolor in reprehenderit in voluptate velit esse cillum dolore eu fugiat nulla pariatur. Excepteur sint occaecat cupidatat non proident, sunt in culpa qui officia deserunt mollit anim id est laborum.</p>
      <p>Lorem ipsum dolor sit amet, consectetur adipisicing elit, sed do eiusmod tempor incididunt ut labore et dolore magna aliqua. Ut enim ad minim veniam, quis nostrud exercitation ullamco laboris nisi ut aliquip ex ea commodo consequat. Duis aute irure dolor in reprehenderit in voluptate velit esse cillum dolore eu fugiat nulla pariatur. Excepteur sint occaecat cupidatat non proident, sunt in culpa qui officia deserunt mollit anim id est laborum.</p>
      <p>Lorem ipsum dolor sit amet, consectetur adipisicing elit, sed do eiusmod tempor incididunt ut labore et dolore magna aliqua. Ut enim ad minim veniam, quis nostrud exercitation ullamco laboris nisi ut aliquip ex ea commodo consequat. Duis aute irure dolor in reprehenderit.</p>
      <p>Yours Sincerely,</p>
      <div class="signature" role="img" aria-label="Handwritten signature"></div>
    </div>
    <footer class="letter-footer">
      <div><strong>Brightpath Wordworks, LLC</strong> 418 Garvin St. Indianapolis, IN 46871</div>
      <div class="contact-row">
        <span class="contact-line"><svg><use href="#icon-phone"/></svg>(317) 584-2316</span>
        <span class="contact-line"><svg><use href="#icon-mail"/></svg>info@brightpathwordworks.com</span>
        <span class="contact-line"><svg><use href="#icon-web"/></svg>www.brightpathwordworks.com</span>
      </div>
    </footer>
  </article>
</main>
</body>
</html>
```